Qorva - Web Design Rebrand for Talent Resourcing Company

I need a new brand for a customer based in Ireland.
The website currently: https://braddick.io/
Qorva repositioning themselves to be strategic talent resourcing and operational technology consultancy, Specialising in Life Sciences and Data Centres.
Essentially their USP:
They have lots of specialist manufacturing & automation resources that understand the Life Sciences Industry

Competitor websites:
https://vernhollow.com/ I really like the clarity on this site and the pink/yellow mix could be replaced with a green/blue mix for Qorva?
https://tulimark.com/ These are a big company so anything we could steal would be good 😊

They want:
• Fresh, sharp imagery
• Movement on the main page (Margot is obsessed with this lol) so may be video on some sections?
• The facility to upload CVs so similar to above.
• A page to show types of jobs available
• A page to show types of resource available from Qorva
• About us
• Sectors they operate in (includes Life Sciences, Food & Bev, Data Centres)

Target Market(s)

HR/Recruitment/Talent Acquisition/Operations Personnel in Life Sciences and Data Centres

Industry/Entity Type

Life Sciences and Data Centres

Number of Pages Required

1 page

Font styles to use
Sans Serif

Colors
0054AA
0677BA
7BADD7
CADEEF
E8F1F8
0094D4
00A9DD
6FCCEA
C7EBF8
E9F6FB
00AB8E
00BBA5
67D7C9
C6EFE9
E9F9F6

Requirements
Must have
• Brand Colour might be green/blue mix OR if another colour combo compelling
Nice to have
• Fresh, Sharp imagery. Movement on the main image (maybe partial video)

```html
<!DOCTYPE html>
<html lang="en">
<head>
<meta charset="utf-8">
<title>Qorva – Strategic Talent Resourcing</title>
<link rel="stylesheet" href="https://fonts.googleapis.com/css2?family=Jost:wght@400;500;600;700&family=Inter:wght@400;500;600;700&display=swap">
<style>
:root{
  --navy:#0054AA;
  --blue:#0677BA;
  --sky:#7BADD7;
  --pale-blue:#CADEEF;
  --ice:#E8F1F8;
  --cyan:#0094D4;
  --teal:#00AB8E;
  --teal-2:#00BBA5;
  --mint:#E9F6F3;
  --about-bg:#CBE9F7;
  --ink:#1b1b1b;
  --logo:#0b5560;
  --footer-dark:#2b2b2b;
  --rule:#a9d6ea;
}
*{box-sizing:border-box;margin:0;padding:0}
html,body{width:1200px;height:3033px;overflow:hidden}
body{position:relative;background:#fff;font-family:'Inter',sans-serif;color:var(--ink)}

/* header */
.site-header{position:absolute;left:0;top:0;width:1200px;height:67px;background:#f7f7f7;z-index:5}
.brand{position:absolute;left:127px;top:12px;font-family:'Jost',sans-serif;font-weight:700;font-size:36px;color:var(--logo);letter-spacing:-0.5px}
.main-nav{position:absolute;left:388px;top:27px;display:flex}
.main-nav a{font-size:10px;color:#222;text-decoration:none;margin-right:30px}
.upload-cv{position:absolute;left:983px;top:26px;font-size:10px;color:var(--blue);text-decoration:underline}
.search-icon{position:absolute;left:1055px;top:23px}

/* hero */
.hero{position:absolute;left:0;top:67px;width:1200px;height:616px;
  background:linear-gradient(105deg,rgba(15,70,140,.95) 0%,rgba(20,100,170,.85) 45%,rgba(10,130,140,.9) 100%),
  linear-gradient(180deg,#3d6f9f,#2d7d8a)}
.hero-title{position:absolute;left:0;top:118px;width:1200px;text-align:center;font-family:'Jost',sans-serif;font-weight:600;font-size:48px;line-height:50px;color:#fff}
.hero-accent{position:absolute;left:0;top:218px;width:1200px;text-align:center;font-family:'Jost',sans-serif;font-weight:600;font-size:46px;color:transparent;-webkit-text-stroke:1.5px #fff}
.hero-rule{position:absolute;left:560px;top:296px;width:80px;height:1px;background:rgba(255,255,255,.7)}
.hero-sub{position:absolute;left:0;top:324px;width:1200px;text-align:center;font-size:14px;letter-spacing:.3px;color:#fff;font-weight:500}
.btn-light{position:absolute;left:525px;top:375px;width:150px;height:41px;background:#cfe2ef;border:1px solid #9fc3db;border-radius:2px;font-size:11px;font-weight:700;color:var(--navy);display:flex;align-items:center;justify-content:center}
.slide-dots{position:absolute;left:52px;top:195px}

/* about */
.about-photo{position:absolute;left:125px;top:552px;width:950px;height:490px;
  background:linear-gradient(100deg,#5b6b5f 0%,#d8d4cc 25%,#e9e6e0 45%,#8a9197 70%,#4d6a80 100%)}
.about-mint{position:absolute;left:0;top:1058px;width:607px;height:99px;background:var(--mint)}
.about-card{position:absolute;left:622px;top:640px;width:410px;height:517px;background:var(--about-bg);padding:40px 53px}
.about-card h2{font-family:'Jost',sans-serif;font-weight:600;font-size:37px;line-height:1;margin-bottom:27px}
.outline-blue{color:transparent;-webkit-text-stroke:1.4px var(--blue)}
.about-card p{font-size:11.3px;line-height:18.3px;margin-bottom:18px;color:#222}
.btn-teal{display:flex;align-items:center;justify-content:center;background:var(--teal);color:#fff;font-size:10.5px;font-weight:700;border-radius:2px}
.about-card .btn-teal{width:150px;height:41px;margin-top:19px}

/* team */
.team-title{position:absolute;left:0;top:1246px;width:1200px;text-align:center;font-family:'Jost',sans-serif;font-weight:600;font-size:37px;line-height:1}
.team-accent{position:absolute;left:0;top:1298px;width:1200px;text-align:center;font-family:'Jost',sans-serif;font-weight:600;font-size:34px;line-height:1}
.team-intro{position:absolute;left:220px;top:1363px;width:760px;text-align:center;font-size:11px;line-height:18px;color:var(--ink)}
.team-intro p+p{margin-top:18px}
.rule{position:absolute;left:125px;width:950px;height:1px}
.featured{position:absolute;left:0;top:1498px;width:1200px;text-align:center;font-family:'Jost',sans-serif;font-weight:500;font-size:23px}

.role{position:absolute;width:302px;text-align:center}
.role-photo{width:302px;height:182px;background:
  linear-gradient(to bottom right,transparent 50%,rgba(10,90,180,.88) 50%,rgba(10,150,160,.85) 100%),
  linear-gradient(135deg,var(--photo-a),var(--photo-b))}
.role h3{margin-top:37px;font-family:'Jost',sans-serif;font-weight:500;font-size:16.5px}
.role p{margin:14px auto 0;width:250px;font-size:11.2px;line-height:18px}
.role .btn-teal{width:232px;height:36px;margin:25px auto 0}

/* stats */
.stats{position:absolute;left:0;top:2508px;width:1200px;height:214px;background:linear-gradient(100deg,#0656a6 0%,#0677BA 45%,#00958f 100%)}
.stat{position:absolute;top:29px;width:302px;height:158px;background:rgba(255,255,255,.3);text-align:center;color:#fff}
.stat strong{display:block;margin-top:26px;font-family:'Jost',sans-serif;font-weight:500;font-size:58px;line-height:1}
.stat span{display:block;margin:8px auto 0;width:170px;font-size:11px;line-height:18px;color:#e6f2fa}

/* footer */
.footer-brand{position:absolute;left:128px;top:2810px;font-family:'Jost',sans-serif;font-weight:700;font-size:62px;line-height:1;color:var(--logo)}
.footer-div{position:absolute;top:2832px;width:1px;height:28px;background:#333}
.footer-links{position:absolute;top:2826px;font-size:11.5px;line-height:28px}
.social{position:absolute;top:2836px;width:24px;height:24px;border-radius:50%}
.copyright{position:absolute;left:0;top:2970px;width:1200px;height:63px;background:var(--footer-dark);color:#eee;font-size:11.5px;display:flex;align-items:center;justify-content:center}
</style>
</head>
<body>

<header class="site-header">
  <div class="brand">Qorva</div>
  <nav class="main-nav">
    <a>Home</a><a>About Us</a><a>Capabilities</a><a>Our Clients</a><a>Join Our Team</a><a>Contact</a>
  </nav>
  <a class="upload-cv">Upload CV</a>
  <svg class="search-icon" width="20" height="20" viewBox="0 0 20 20" fill="none" stroke="#0677BA" stroke-width="2"><circle cx="8" cy="8" r="6"/><line x1="12.5" y1="12.5" x2="18" y2="18"/></svg>
</header>

<section class="hero" role="img" aria-label="Team of professionals working at a meeting table, under a blue to teal overlay">
  <h1 class="hero-title">Strategic Talent Resourcing &amp;<br>Operational Technology</h1>
  <div class="hero-accent">Export</div>
  <div class="hero-rule"></div>
  <div class="hero-sub">SPECIALISING IN LIFE SCIENCES AND DATA CENTRES</div>
  <div class="btn-light">Contact Us</div>
  <svg class="slide-dots" width="12" height="214" viewBox="0 0 12 214" fill="none" stroke="#fff" stroke-width="1.2">
    <circle cx="6" cy="5" r="4" fill="#fff"/>
    <line x1="6" y1="9" x2="6" y2="47"/><circle cx="6" cy="51" r="4"/>
    <line x1="6" y1="55" x2="6" y2="97"/><circle cx="6" cy="101" r="4"/>
    <line x1="6" y1="105" x2="6" y2="149"/><circle cx="6" cy="153" r="4"/>
    <line x1="6" y1="157" x2="6" y2="201"/><circle cx="6" cy="205" r="4"/>
  </svg>
</section>

<div class="about-mint"></div>
<div class="about-photo" role="img" aria-label="Smiling young professional in glasses taking notes in a bright office, colleague behind"></div>
<section class="about-card">
  <h2>About <span class="outline-blue">Qorva</span></h2>
  <p>Qorva is proud to be providing top-tier resources to the life sciences sector, specialising in delivering high-quality talent and solutions that enhance the capabilities and operational excellence of our customers.</p>
  <p>Our operational technology expertise and talent pool has evolved over the past decade with successful project delivery for numerous life sciences organisations , so we are uniquely positioned to understand and meet your requirements.</p>
  <p>We are focused on matching the dynamic needs of life sciences firms with skilled professionals, thereby driving innovation and growth in this critical sector across Ireland.</p>
  <div class="btn-teal">Read More</div>
</section>

<h2 class="team-title">Meat Qorva</h2>
<div class="team-accent outline-blue">Team</div>
<div class="team-intro">
  <p>Qorva employees have a variety of skills and experience, but they all are professional, experienced in their field and enjoy the variety of working at different client sites over time.</p>
  <p>They get a feeling of success seeing a project through to completion, and are always willing to go the extra mile for our clients.</p>
</div>
<div class="rule" style="top:1480px;background:var(--rule)"></div>
<h2 class="featured">Featured roles</h2>
<div class="rule" style="top:1545px;background:#dcdcdc"></div>

<article class="role" style="left:125px;top:1572px">
  <div class="role-photo" style="--photo-a:#8d8a84;--photo-b:#d8d2c8" role="img" aria-label="Colleagues collaborating in an office"></div>
  <h3>Automation &amp; CSV</h3>
  <p>Lorem Ipsum is simply dummy text of the printing and typesetting industry. Lorem Ipsum has been the industry's standard dummy text ever since the 1500s,</p>
  <div class="btn-teal">Explore Automation/CSV Jobs</div>
</article>
<article class="role" style="left:448px;top:1572px">
  <div class="role-photo" style="--photo-a:#2d4f6a;--photo-b:#9fb4c2" role="img" aria-label="Scientist in mask with molecular graphics"></div>
  <h3>Bioprocess</h3>
  <p>Lorem Ipsum is simply dummy text of the printing and typesetting industry. Lorem Ipsum has been the industry's standard dummy text ever since the 1500s,</p>
  <div class="btn-teal">Explore Bioprocess jobs</div>
</article>
<article class="role" style="left:772px;top:1572px">
  <div class="role-photo" style="--photo-a:#3a3f46;--photo-b:#8c8f7a" role="img" aria-label="Technicians in hard hats inspecting equipment"></div>
  <h3>Commissioning &amp; Validation</h3>
  <p>Lorem Ipsum is simply dummy text of the printing and typesetting industry. Lorem Ipsum has been the industry's standard dummy text ever since the 1500s,</p>
  <div class="btn-teal">Explore CQV Jobs</div>
</article>

<article class="role" style="left:125px;top:2015px">
  <div class="role-photo" style="--photo-a:#7b6a58;--photo-b:#d9d3c8" role="img" aria-label="Engineers reviewing plans on site"></div>
  <h3>Engineering</h3>
  <p>Lorem Ipsum is simply dummy text of the printing and typesetting industry. Lorem Ipsum has been the industry's standard dummy text ever since the 1500s,</p>
  <div class="btn-teal">Explore Engineering Jobs</div>
</article>
<article class="role" style="left:448px;top:2015px">
  <div class="role-photo" style="--photo-a:#2e2c2b;--photo-b:#8d8478" role="img" aria-label="Project team meeting in front of a presentation screen"></div>
  <h3>Project Management</h3>
  <p>Lorem Ipsum is simply dummy text of the printing and typesetting industry. Lorem Ipsum has been the industry's standard dummy text ever since the 1500s,</p>
  <div class="btn-teal">Explore Engineering Jobs</div>
</article>
<article class="role" style="left:772px;top:2015px">
  <div class="role-photo" style="--photo-a:#5e86a8;--photo-b:#c9dbe8" role="img" aria-label="Laboratory analyst using a microscope"></div>
  <h3>QC &amp; Laboratory</h3>
  <p>Lorem Ipsum is simply dummy text of the printing and typesetting industry. Lorem Ipsum has been the industry's standard dummy text ever since the 1500s,</p>
  <div class="btn-teal">Explore QC &amp; Lab jobs</div>
</article>

<section class="stats">
  <div class="stat" style="left:125px"><strong>50+</strong><span>Number skilled automation engineers</span></div>
  <div class="stat" style="left:448px"><strong>25+</strong><span>Customers currently using Qorva</span></div>
  <div class="stat" style="left:772px"><strong>99%</strong><span>Customer retention</span></div>
</section>

<footer>
  <div class="footer-brand">Qorva</div>
  <div class="footer-div" style="left:395px"></div>
  <div class="footer-links" style="left:445px">Home<br>About Us</div>
  <div class="footer-div" style="left:553px"></div>
  <div class="footer-links" style="left:603px">Capabilities<br>Our Clients</div>
  <div class="footer-div" style="left:727px"></div>
  <div class="footer-links" style="left:777px">Join Our Team<br>Contact</div>
  <div class="footer-div" style="left:917px"></div>
  <div class="social" style="left:967px;background:var(--blue)" aria-label="Social link"></div>
  <div class="social" style="left:1006px;background:var(--cyan)" aria-label="Social link"></div>
  <div class="social" style="left:1046px;background:#111" aria-label="Social link"></div>
  <div class="copyright">Copyright 2024-Qorva-All rights reserved</div>
</footer>

</body>
</html>
```